Brevik Fabrication - Business Card Design

We would like a dark (likely black) themed business card to be able to hand out to potential clients. We may list our services on the card or keep it clean. Unsure. Logo attached

```html
<!DOCTYPE html>
<html lang="en">
<head>
<meta charset="utf-8">
<title>Brevik Fabrication – Business Card</title>
<link rel="stylesheet" href="https://fonts.googleapis.com/css2?family=Roboto+Condensed:wght@400;700&display=swap">
<style>
  :root {
    --page: #e2e1e1;
    --card-dark: #231f20;
    --brand-blue: #1b6fb8;
    --brand-orange: #f15a24;
    --text-light: #e6e6e6;
    --white: #ffffff;
  }
  * { box-sizing: border-box; margin: 0; padding: 0; }
  html, body {
    width: 1125px; height: 1200px; overflow: hidden;
    background: var(--page);
    font-family: "Roboto Condensed", "Arial Narrow", sans-serif;
  }
  .card {
    position: absolute; left: 171px; width: 826px; height: 472px;
    border-radius: 26px; overflow: hidden;
    background: var(--card-dark);
    box-shadow: 2px 4px 6px rgba(0,0,0,0.35);
  }
  .card--front { top: 106px; }
  .card--back { top: 639px; }

  .front-wave { position: absolute; inset: 0; width: 100%; height: 100%; }

  .holder { position: absolute; right: 64px; top: 42px; text-align: right; }
  .holder__name { color: var(--white); font-weight: 700; font-size: 31px; line-height: 1.1; }
  .holder__title { color: var(--brand-orange); font-size: 21px; line-height: 1.2; }

  .address {
    position: absolute; left: 51px; top: 197px;
    color: var(--text-light); font-size: 21px; line-height: 25px;
  }
  .contacts {
    position: absolute; left: 51px; top: 284px; list-style: none;
    color: var(--text-light); font-size: 21px; line-height: 25.5px;
  }
  .contacts li { display: flex; align-items: center; gap: 10px; }
  .contacts svg { width: 19px; height: 19px; fill: var(--brand-blue); flex: none; }

  .brand-mark { position: absolute; left: 468px; top: 240px; width: 300px; text-align: center; }
  .brand-mark__dot {
    display: block; width: 84px; height: 84px; margin: 0 auto 18px;
    border-radius: 50%; background: var(--brand-orange);
  }
  .brand-mark__name {
    color: var(--brand-blue); font-weight: 700; font-size: 38px;
    text-transform: uppercase; line-height: 1;
  }

  .back-name {
    position: absolute; left: 61px; top: 44px;
    color: var(--brand-blue); font-weight: 700; font-size: 46px;
    text-transform: uppercase; line-height: 1;
  }
  .services {
    position: absolute; left: 61px; top: 134px; list-style: none;
    color: var(--text-light); font-size: 21px; line-height: 28px;
  }
  .services li { display: flex; align-items: center; gap: 12px; }
  .services li::before {
    content: ""; width: 6px; height: 6px; border-radius: 50%;
    background: var(--brand-blue);
  }
  .back-emblem {
    position: absolute; left: 444px; top: 69px; width: 420px; height: 420px;
    border-radius: 50%; background: var(--brand-orange);
  }
</style>
</head>
<body>
  <section class="card card--front">
    <svg class="front-wave" viewBox="0 0 800 457" preserveAspectRatio="none" aria-hidden="true">
      <rect width="800" height="457" fill="var(--brand-blue)"/>
      <path d="M0 165 C110 45 250 50 390 95 C530 140 660 160 800 125 V457 H0 Z" fill="var(--card-dark)"/>
      <path d="M5 160 C112 52 250 58 390 103 C530 148 660 166 800 132 V457 H0 Z" fill="var(--brand-orange)"/>
      <path d="M0 168 C112 62 250 70 390 113 C530 156 660 170 800 136 V457 H0 Z" fill="var(--card-dark)"/>
      <path d="M0 171 C112 70 250 78 390 121 C530 164 660 174 800 139 V457 H0 Z" fill="var(--brand-blue)"/>
      <path d="M0 180 C112 80 250 88 390 130 C530 170 660 176 800 140 V457 H0 Z" fill="var(--card-dark)"/>
    </svg>

    <div class="holder">
      <p class="holder__name">Daniel Okafor</p>
      <p class="holder__title">President</p>
    </div>

    <address class="address" style="font-style:normal">
      Brevik Fabrication Inc<br>
      4120 Alder Ridge Road<br>
      Kettle Bay, Alaska 34590
    </address>

    <ul class="contacts">
      <li><svg viewBox="0 0 24 24"><path d="M6.6 10.8a15 15 0 0 0 6.6 6.6l2.2-2.2c.3-.3.7-.4 1-.2 1.1.4 2.3.6 3.6.6.6 0 1 .4 1 1V20c0 .6-.4 1-1 1A17 17 0 0 1 3 4c0-.6.4-1 1-1h3.5c.6 0 1 .4 1 1 0 1.3.2 2.5.6 3.6.1.3 0 .7-.2 1z"/></svg>369-740-2216</li>
      <li><svg viewBox="0 0 24 24"><path d="M7 1h10a2 2 0 0 1 2 2v18a2 2 0 0 1-2 2H7a2 2 0 0 1-2-2V3a2 2 0 0 1 2-2zm0 3v15h10V4z"/></svg>369-618-3094</li>
      <li><svg viewBox="0 0 24 24"><path d="M6 2h12v5H6zM3 8h18a2 2 0 0 1 2 2v7h-4v5H5v-5H1v-7a2 2 0 0 1 2-2zm4 8v4h10v-4z"/></svg>369-455-7102</li>
      <li><svg viewBox="0 0 24 24"><path d="M2 5h20v14H2zm2 2v.5l8 5 8-5V7z"/></svg>info@brevikfabrication.com</li>
      <li><svg viewBox="0 0 24 24"><circle cx="12" cy="12" r="10"/></svg>www.brevikfabrication.com</li>
    </ul>

    <div class="brand-mark">
      <span class="brand-mark__dot" aria-hidden="true"></span>
      <p class="brand-mark__name">Brevik Fabrication</p>
    </div>
  </section>

  <section class="card card--back">
    <p class="back-name">Brevik Fabrication</p>
    <ul class="services">
      <li>AC Installation &amp; Replacement</li>
      <li>AC Maintenance</li>
      <li>AC Repair</li>
      <li>Heater Repair</li>
      <li>Heater Installation</li>
      <li>Heater Maintenance</li>
      <li>Duct Cleaning</li>
      <li>Duct Repair</li>
      <li>Duct Installation</li>
      <li>Air Quality</li>
      <li>Thermostats</li>
    </ul>
    <div class="back-emblem" aria-hidden="true"></div>
  </section>
</body>
</html>
```